The Molar Nook Dental Offices Double-Sided A5 Flyer Highlighting Strengths & All Locations.

Designs are looking good. I just feel that they're too much in terms of content. Slight change in strategy. I would like a double sided A5 Flyer that has the following:

Front Side:

1. Brand (The Molar Nook Dental Offices). Use the logo that has Dental Offices beneath the words "The Molar Nook."
2. Highlight only the following keywords: Affordable. Friendly. Experienced Dental Care. Kids Friendly. We Accept All Insurance. 0% Interest Payment Plans.
3. Dental Services: Family Dentistry, Teeth Whitening, Braces, Implants, Veneers, Sedation.

Back Side:

This is where I want to highlight how convenient The Molar Nook is. We have 15 locations and growing. So here you can use our tagline:

We're Always Close to Home! With 15 Locations and Growing.

I want to list all 15 locations with each locations address and unique number. You can find those at https://molarnookexample.com/locations
The designer that can provide all locations in a catchy, easy to read and clean design will be selected.

The base of the flyer should utilize a white background. Keep it clean. Keep it fresh.

I'm looking to stand out from all competition with something unique and different. Get creative.

Target Market(s)

Women 30-40 years of age.

Industry/Entity Type

Dental

Font styles to use
Sans Serif

Colors
86cfc6
33b8a4
00a990
f59195
fdfdfb
fdf9cf
dddddd

Requirements
Must have
• Proper brand and color elements. Use white background.
Nice to have
• Surprise me with great ideas and design.
Should not have
• Prices.

```html
<!DOCTYPE html>
<html lang="en">
<head>
<meta charset="utf-8">
<title>The Molar Nook Dental Offices – A5 Flyer</title>
<link href="https://fonts.googleapis.com/css2?family=Raleway:wght@400;500;600;700&display=swap" rel="stylesheet">
<style>
  :root {
    --stage: #474747;
    --paper: #ffffff;
    --green: #a3d4b1;
    --green-text: #86c9a0;
    --blue: #86c7ee;
    --blue-text: #6ab6e4;
    --pink: #f0878c;
    --purple: #c89ae8;
    --ink: #5c5c5c;
    --ink-soft: #777777;
  }
  * { box-sizing: border-box; margin: 0; padding: 0; }
  html, body {
    width: 960px; height: 1200px; overflow: hidden;
    background: var(--stage);
    font-family: 'Raleway', sans-serif;
    color: var(--ink);
  }
  .icon-defs { position: absolute; width: 0; height: 0; }

  .flyer {
    position: absolute; left: 98px; width: 746px; height: 499px;
    background: var(--paper); overflow: hidden;
  }
  .flyer--front { top: 70px; }
  .flyer--back { top: 626px; }

  /* Front */
  .front-backdrop {
    position: absolute; left: 0; top: 0; width: 420px; height: 499px;
    background: radial-gradient(ellipse at 55% 45%, #f3f1ef 0%, #fbfaf9 45%, #ffffff 75%);
  }
  .brand { position: absolute; left: 32px; top: 62px; display: flex; align-items: center; gap: 12px; }
  .brand__dot { width: 44px; height: 44px; border-radius: 50%; background: var(--green); }
  .brand__name { font-size: 30px; font-weight: 500; color: #6b6b6b; line-height: 1; white-space: nowrap; }
  .brand__sub { font-size: 9.5px; font-weight: 500; color: #6b6b6b; letter-spacing: 1px; margin-top: 6px; text-align: right; }

  .pitch { position: absolute; left: 35px; top: 188px; color: var(--green-text); font-size: 20px; line-height: 24px; font-weight: 400; letter-spacing: .3px; }
  .pitch--kids { top: 259px; }
  .pitch__note { position: absolute; left: 35px; top: 290px; color: var(--pink); font-size: 12.5px; letter-spacing: .4px; }

  .band { position: absolute; left: 0; width: 746px; color: #fff; display: flex; align-items: center; padding-left: 35px; letter-spacing: .3px; white-space: nowrap; }
  .band--services { top: 328px; height: 44px; background: var(--pink); font-size: 14px; z-index: 3; }
  .band--sleep { top: 379px; height: 34px; background: var(--blue); font-size: 14px; padding-left: 37px; z-index: 1; }

  .pin-art { position: absolute; left: 0; top: 0; width: 746px; height: 499px; z-index: 2; }
  .pin-tagline {
    position: absolute; left: 440px; top: 380px; width: 140px; z-index: 4;
    text-align: center; color: #fff; font-size: 13.5px; line-height: 22px; letter-spacing: .3px;
  }
  .badge-plan {
    position: absolute; left: 580px; top: 27px; width: 136px; height: 136px; z-index: 5;
    border-radius: 50%; background: var(--blue); border: 5px solid #fff;
    display: flex; align-items: center; justify-content: center; text-align: center;
    color: #fff; font-size: 16px; line-height: 20px; letter-spacing: .5px;
  }
  .insurance { position: absolute; left: 41px; top: 446px; font-size: 13px; letter-spacing: .5px; color: var(--ink); }
  .contact { position: absolute; right: 14px; top: 438px; z-index: 4; text-align: right; }
  .contact__phone { display: flex; align-items: center; justify-content: flex-end; gap: 4px; color: var(--green-text); font-weight: 700; font-size: 18px; }
  .contact__phone svg { width: 13px; height: 13px; fill: var(--green-text); }
  .contact__web { font-size: 13px; color: var(--ink); margin-top: 4px; letter-spacing: .2px; white-space: nowrap; }

  /* Back */
  .headline {
    height: 39px; background: var(--green); color: #fff;
    display: flex; align-items: center; justify-content: center;
    font-size: 16px; font-weight: 400; letter-spacing: .6px; white-space: nowrap;
  }
  .col { position: absolute; top: 58px; width: 170px; }
  .col--1 { left: 18px; } .col--2 { left: 206px; } .col--3 { left: 392px; } .col--4 { left: 578px; width: 160px; }

  .loc { position: relative; margin-bottom: 13px; }
  .loc__city { font-size: 14px; font-weight: 700; color: var(--blue-text); line-height: 21px; letter-spacing: .4px; }
  .loc__name { font-size: 11.5px; font-weight: 700; color: var(--green-text); line-height: 19px; letter-spacing: .4px; white-space: nowrap; }
  .loc__addr { position: relative; padding-left: 13px; font-size: 9.5px; line-height: 13.5px; color: var(--ink-soft); }
  .loc__addr::before {
    content: ""; position: absolute; left: 1px; top: 2px; width: 6px; height: 6px;
    border: 2px solid var(--green-text); border-radius: 50% 50% 50% 0; transform: rotate(-45deg);
  }
  .loc__phone { display: flex; align-items: center; gap: 3px; font-size: 9.5px; line-height: 16px; color: var(--ink-soft); margin-top: 2px; }
  .loc__phone svg { width: 8px; height: 8px; fill: var(--green-text); }
  .pill {
    margin-left: 8px; padding: 3px 9px; border-radius: 11px; background: var(--purple);
    color: #fff; font-size: 6.5px; font-weight: 700; line-height: 7.5px; text-align: center; letter-spacing: .3px;
  }
  .tag {
    position: absolute; right: 0; top: 24px; padding: 3px 6px;
    background: var(--pink); color: #fff; border-radius: 3px;
    font-size: 7.5px; font-weight: 700; line-height: 8px; text-align: center; letter-spacing: .4px;
    transform: rotate(-12deg);
  }
  .tag::before {
    content: ""; position: absolute; left: 50%; top: -8px; width: 9px; height: 9px; margin-left: -5px;
    border-left: 1.5px solid var(--pink); border-top: 1.5px solid var(--pink); transform: rotate(45deg);
  }
  .col--1 .loc:first-child .tag { top: 18px; }
  .col--4 .tag { top: 20px; }

  .back-brand { position: absolute; left: 568px; top: 398px; width: 170px; text-align: center; }
  .back-brand__dot { width: 34px; height: 34px; border-radius: 50%; background: var(--green); margin: 0 auto 8px; }
  .back-brand__name { font-size: 19px; font-weight: 500; color: #6b6b6b; line-height: 1; white-space: nowrap; }
  .back-brand__sub { font-size: 6.5px; font-weight: 500; color: #6b6b6b; letter-spacing: .8px; margin-top: 4px; }
</style>
</head>
<body>

<svg class="icon-defs" aria-hidden="true">
  <defs>
    <symbol id="phone" viewBox="0 0 24 24">
      <path d="M6.6 10.8c1.4 2.8 3.8 5.1 6.6 6.6l2.2-2.2c.3-.3.7-.4 1-.2 1.1.4 2.3.6 3.6.6.6 0 1 .4 1 1V20c0 .6-.4 1-1 1C10.6 21 3 13.4 3 4c0-.6.4-1 1-1h3.5c.6 0 1 .4 1 1 0 1.3.2 2.5.6 3.6.1.3 0 .7-.2 1L6.6 10.8z"/>
    </symbol>
  </defs>
</svg>

<section class="flyer flyer--front" aria-label="Flyer front">
  <div class="front-backdrop" role="img" aria-label="Faint background photo of a smiling woman"></div>

  <div class="brand">
    <span class="brand__dot"></span>
    <div>
      <div class="brand__name">The Molar Nook</div>
      <div class="brand__sub">DENTAL OFFICES</div>
    </div>
  </div>

  <p class="pitch">Experienced and Affordable<br>Family &amp; Cosmetic Dentistry.</p>
  <p class="pitch pitch--kids">We're Kids Friendly.</p>
  <p class="pitch__note">WITH LOCATIONS OPEN 7 DAYS A WEEK</p>

  <svg class="pin-art" viewBox="0 0 746 499">
    <defs>
      <radialGradient id="photoTone" cx="45%" cy="45%" r="65%">
        <stop offset="0%" stop-color="#f4dccd"/>
        <stop offset="55%" stop-color="#d9b39c"/>
        <stop offset="100%" stop-color="#8a5e45"/>
      </radialGradient>
    </defs>
    <path d="M369.7 257 A162 162 0 1 1 650.3 257 L525 474 Q510 500 495 474 Z" fill="var(--green)"/>
    <circle cx="510" cy="170" r="124" fill="#ffffff"/>
    <circle cx="510" cy="172" r="119" fill="url(#photoTone)" role="img" aria-label="Photo of a smiling mother and young daughter cheek to cheek"/>
  </svg>

  <div class="badge-plan">0%<br>INTEREST<br>PAYMENT<br>PLANS.</div>

  <div class="band band--services">FAMILY DENTISTRY • TEETH WHITENING • BRACES • IMPLANTS • VENEERS • SEDATION</div>
  <div class="band band--sleep">WE OFFER SLEEP DENTISTRY.</div>

  <p class="pin-tagline">SMILES ON<br>EVERY<br>CORNER</p>

  <p class="insurance">WE ACCEPT ALL INSURANCE.</p>

  <div class="contact">
    <div class="contact__phone"><svg><use href="#phone"/></svg>1-888-555-0199</div>
    <div class="contact__web">www.molarnookexample.com</div>
  </div>
</section>

<section class="flyer flyer--back" aria-label="Flyer back">
  <h2 class="headline">WE'RE ALWAYS CLOSE TO HOME! WITH 15 LOCATIONS AND GROWING.</h2>

  <div class="col col--1">
    <div class="loc">
      <h3 class="loc__city">BARRIE</h3>
      <h4 class="loc__name">LAKEVIEW MALL</h4>
      <span class="tag">OPEN<br>7 DAYS!</span>
      <p class="loc__addr">410 Lakeview Street<br>Unit T210 (in Lakeview Mall)<br>Barrie ON, L4M 0A1</p>
      <p class="loc__phone"><svg><use href="#phone"/></svg>(705) 555-0141 <span class="pill">SEDATION<br>DENTISTRY</span></p>
    </div>
    <div class="loc">
      <h3 class="loc__city">BRAMPTON</h3>
      <h4 class="loc__name">MAPLEBROOK PLAZA</h4>
      <p class="loc__addr">88 Maplebrook Parkway East,<br>Unit 12, Maplebrook Plaza<br>Brampton ON, L6Z 0A2</p>
      <p class="loc__phone"><svg><use href="#phone"/></svg>905-555-0142</p>
    </div>
    <div class="loc">
      <h3 class="loc__city">BRANTFORD</h3>
      <h4 class="loc__name">ELM CROSS ST.</h4>
      <p class="loc__addr">52 Elm Cross St.<br>Brantford ON, N3R 0A3</p>
      <p class="loc__phone"><svg><use href="#phone"/></svg>(519) 555-0143</p>
    </div>
    <div class="loc">
      <h4 class="loc__name">ASHGROVE ST. W.</h4>
      <p class="loc__addr">276 Ashgrove Street West<br>Unit 2B<br>Brantford ON, N3T 0A4</p>
      <p class="loc__phone"><svg><use href="#phone"/></svg>(519) 555-0144 <span class="pill">SEDATION<br>DENTISTRY</span></p>
    </div>
  </div>

  <div class="col col--2">
    <div class="loc">
      <h3 class="loc__city">DUNDAS</h3>
      <h4 class="loc__name">MILL ST. E.</h4>
      <p class="loc__addr">71 Mill Street East,<br>Unit 4<br>Dundas, ON L9H 0A5</p>
      <p class="loc__phone"><svg><use href="#phone"/></svg>(905) 555-0145</p>
    </div>
    <div class="loc">
      <h3 class="loc__city">ETOBICOKE</h3>
      <h4 class="loc__name">BIRCHWOOD RD.</h4>
      <p class="loc__addr">1800 Birchwood Road,<br>Unit 3<br>Etobicoke ON, M9V 0A6</p>
      <p class="loc__phone"><svg><use href="#phone"/></svg>(416) 555-0146 <span class="pill">SEDATION<br>DENTISTRY</span></p>
    </div>
    <div class="loc">
      <h4 class="loc__name">RIVERBEND BLVD</h4>
      <p class="loc__addr">240 Riverbend Blvd<br>Unit 9<br>Etobicoke, ON M9V 0A7</p>
      <p class="loc__phone"><svg><use href="#phone"/></svg>(416) 555-0147</p>
    </div>
    <div class="loc">
      <h3 class="loc__city">STONEY CREEK</h3>
      <h4 class="loc__name">HAMILTON</h4>
      <p class="loc__addr">315 Ridge Rd., Unit #5<br>Stoney Creek ON, L8G 0A8</p>
      <p class="loc__phone"><svg><use href="#phone"/></svg>905-555-0148</p>
    </div>
  </div>

  <div class="col col--3">
    <div class="loc">
      <h3 class="loc__city">MISSISSAUGA</h3>
      <h4 class="loc__name">ORCHARD RD.</h4>
      <p class="loc__addr">2950 Orchard Road<br>Unit 110<br>Mississauga, ON L4Y 0A9</p>
      <p class="loc__phone"><svg><use href="#phone"/></svg>(905) 555-0149</p>
    </div>
    <div class="loc">
      <h4 class="loc__name">WILLOW RD. E.</h4>
      <p class="loc__addr">3410 Willow Road East<br>Unit 18<br>Mississauga ON, L4T 0B1</p>
      <p class="loc__phone"><svg><use href="#phone"/></svg>(905) 555-0150</p>
    </div>
    <div class="loc">
      <h4 class="loc__name">HARBOUR SQ. MALL</h4>
      <span class="tag">OPEN<br>7 DAYS!</span>
      <p class="loc__addr">290 Harbourview Rd.<br>E. #40 Harbour<br>Square Mall (2nd Floor)<br>Mississauga, ON, L5A 0B2</p>
      <p class="loc__phone"><svg><use href="#phone"/></svg>905-555-0151</p>
    </div>
    <div class="loc">
      <h4 class="loc__name">FERNBROOK ROAD</h4>
      <p class="loc__addr">4700 Fernbrook Rd.<br>Unit # 6<br>Mississauga, Ontario L4W 0B3</p>
      <p class="loc__phone"><svg><use href="#phone"/></svg>905-555-0152</p>
    </div>
  </div>

  <div class="col col--4">
    <div class="loc">
      <h3 class="loc__city">SCARBOROUGH</h3>
      <h4 class="loc__name">NORTHGATE PLAZA</h4>
      <p class="loc__addr">2090 Cedar Ave. East<br>Unit 11<br>Scarborough ON, M1R 0B4</p>
      <p class="loc__phone"><svg><use href="#phone"/></svg>(416) 555-0153 <span class="pill">SEDATION<br>DENTISTRY</span></p>
    </div>
    <div class="loc">
      <h4 class="loc__name">LAKESHORE SQUARE</h4>
      <span class="tag">OPEN<br>7 DAYS!</span>
      <p class="loc__addr">4380B Lakeshore Rd.<br>Scarborough<br>ON, M1E 0B5</p>
      <p class="loc__phone"><svg><use href="#phone"/></svg>(416) 555-0154</p>
    </div>
    <div class="loc">
      <h4 class="loc__name">POPLAR RD.</h4>
      <p class="loc__addr">1850 Poplar Road<br>Unit 3<br>Scarborough ON, M1P 0B6</p>
      <p class="loc__phone"><svg><use href="#phone"/></svg>(416) 555-0155</p>
    </div>
  </div>

  <div class="back-brand">
    <div class="back-brand__dot"></div>
    <div class="back-brand__name">The Molar Nook</div>
    <div class="back-brand__sub">DENTAL OFFICES</div>
  </div>
</section>

</body>
</html>
```